Saucy Velvet Impz Business Card

We need business cards designed for our consultants to use and hand out to customers.
We are an Adult party plan company (like Crelvaware but sex toys and lingerie)
We would like bright colours pinks, purples.
The cards need our logo
Space for the reps phone number email address and name.
We need our website on it www.saucyvelvetimps.com.au

```html
<!DOCTYPE html>
<html lang="en">
<head>
<meta charset="utf-8">
<title>Saucy Velvet Impz — Business Card</title>
<link href="https://fonts.googleapis.com/css2?family=Archivo+Black&family=Questrial&display=swap" rel="stylesheet">
<style>
  :root {
    --page-bg: #ecebe8;
    --card-black: #141414;
    --card-charcoal: #222222;
    --plum: #8e1a5c;
    --plum-deep: #5e0f3b;
    --plum-bright: #a3236c;
    --pink: #e46aa8;
    --pink-soft: #f2a8cc;
    --ink: #111111;
    --rule: #3b0a26;
  }
  * { box-sizing: border-box; margin: 0; padding: 0; }
  html, body { width: 1200px; height: 900px; overflow: hidden; }
  body { background: var(--page-bg); position: relative; font-family: "Questrial", sans-serif; }

  .card {
    position: absolute;
    width: 560px; height: 320px;
    overflow: hidden;
    box-shadow: 0 10px 30px rgba(0,0,0,.25);
  }

  /* ---------- Front ---------- */
  .card--front { left: 110px; top: 90px; background: var(--card-charcoal); }
  .front__left {
    position: absolute; left: 0; top: 0; width: 215px; height: 100%;
    background: var(--card-black);
  }
  .front__left-strip {
    position: absolute; left: 0; bottom: 48px; width: 215px; height: 26px;
    background: var(--plum);
  }
  .front__mark {
    position: absolute; left: 78px; top: 110px; width: 70px; height: 70px;
    border-radius: 50%; background: var(--pink);
  }
  .front__pattern {
    position: absolute; right: 20px; top: 20px; width: 300px; height: 150px;
    background: radial-gradient(ellipse at center, rgba(242,168,204,.55), rgba(142,26,92,.15) 70%, transparent);
  }
  .front__band {
    position: absolute; left: 215px; top: 176px; right: 0; height: 46px;
    background: var(--plum);
    display: flex; align-items: center; justify-content: center;
  }
  .brand-name {
    font-family: "Archivo Black", sans-serif;
    font-size: 26px; color: var(--ink); letter-spacing: .5px;
  }

  /* ---------- Back ---------- */
  .card--back {
    left: 530px; top: 480px;
    background: linear-gradient(135deg, var(--plum-bright), var(--plum) 55%, var(--plum-deep));
  }
  .back__left {
    position: absolute; left: 0; top: 0; width: 200px; height: 100%;
    background: var(--card-black);
  }
  .back__left-strip {
    position: absolute; left: 0; top: 0; width: 40px; height: 100%;
    background: var(--plum);
  }
  .back__mark {
    position: absolute; left: 72px; top: 125px; width: 56px; height: 56px;
    border-radius: 50%; background: var(--pink);
  }
  .back__brand {
    position: absolute; left: 160px; top: 160px;
    transform: translate(-50%, -50%) rotate(-90deg);
    white-space: nowrap;
    font-family: "Archivo Black", sans-serif; font-size: 24px;
    color: var(--pink);
  }
  .back__pattern {
    position: absolute; left: 260px; top: 40px; width: 260px; height: 150px;
    background: radial-gradient(ellipse at center, rgba(242,168,204,.22), transparent 70%);
  }
  .contact { position: absolute; left: 230px; top: 34px; width: 300px; color: var(--ink); }
  .contact__name { font-family: "Archivo Black", sans-serif; font-size: 21px; text-align: center; }
  .contact__role { font-size: 13px; text-align: center; margin-bottom: 10px; }
  .contact__rule { border: none; border-top: 1px solid var(--rule); margin: 10px 0; }
  .contact__line { display: flex; align-items: center; gap: 12px; font-size: 15px; margin: 6px 0 6px 14px; }
  .contact__line svg { width: 13px; height: 13px; fill: var(--ink); flex: none; }
  .contact__web { font-size: 17px; margin-top: 16px; }
</style>
</head>
<body>

<section class="card card--front" aria-label="Business card front">
  <div class="front__left"></div>
  <div class="front__left-strip"></div>
  <div class="front__mark"></div>
  <div class="front__pattern" role="img" aria-label="Decorative cluster of overlapping pink rounded squares"></div>
  <div class="front__band"><span class="brand-name">Saucy Velvet Impz</span></div>
</section>

<section class="card card--back" aria-label="Business card back">
  <div class="back__left"></div>
  <div class="back__left-strip"></div>
  <div class="back__mark"></div>
  <div class="back__brand">Saucy Velvet Impz</div>
  <div class="back__pattern" role="img" aria-label="Faint decorative rounded squares"></div>

  <div class="contact">
    <p class="contact__name">Alex Moreau</p>
    <p class="contact__role">general manager</p>
    <hr class="contact__rule">
    <p class="contact__line">
      <svg viewBox="0 0 24 24"><path d="M6.6 10.8a15 15 0 0 0 6.6 6.6l2.2-2.2c.3-.3.7-.4 1-.2 1.1.4 2.3.6 3.6.6.6 0 1 .4 1 1V20c0 .6-.4 1-1 1A17 17 0 0 1 3 4c0-.6.4-1 1-1h3.5c.6 0 1 .4 1 1 0 1.3.2 2.5.6 3.6.1.3 0 .7-.2 1z"/></svg>
      +01 555 0192
    </p>
    <p class="contact__line">
      <svg viewBox="0 0 24 24"><path d="M2 5h20v14H2zm2 2v.4l8 5 8-5V7zm0 2.8V17h16V9.8l-8 5z"/></svg>
      moreau@saucyvelvetimps.com
    </p>
    <hr class="contact__rule">
    <p class="contact__line contact__web">
      <svg viewBox="0 0 24 24"><path d="M12 3l10 9h-3v8h-5v-6h-4v6H5v-8H2z"/></svg>
      www.saucyvelvetimps.com.au
    </p>
  </div>
</section>

</body>
</html>
```